Stationery design for BrookSpan
Letterhead, Business card and envelope
Project: Stationery design for BrookSpan
Stationery design for BrookSpan -
Creative Brief
Simple
Name Surname
Director, Fixed Income & Currencies Trading
BrookSpan Associates Limited Harbor Court 17, Oduya Close Eastmere I Coralton I Westland
Dayo@brook-span.example
RC 482316
For Letterhead and Envelope, Details are; BrookSpan Associates Limited Harbor Court, 17, Oduya Close Eastmere I Coralton I Westland contact@brook-span.example +234 (1) 5558214

```html
<!DOCTYPE html>
<html lang="en">
<head>
<meta charset="utf-8">
<title>BrookSpan Business Card</title>
<link rel="stylesheet" href="https://fonts.googleapis.com/css2?family=Open+Sans:wght@400;600;700&display=swap">
<style>
  :root {
    --page-bg: #e7e4df;
    --card-bg: #ffffff;
    --ink: #1f1f1f;
    --ink-soft: #555555;
    --accent-red: #b23a2a;
    --rule: #c9c9c9;
  }
  html, body {
    margin: 0;
    padding: 0;
    width: 1200px;
    height: 816px;
    overflow: hidden;
    background: var(--page-bg);
    font-family: "Open Sans", Arial, sans-serif;
  }
  .canvas {
    position: relative;
    width: 1200px;
    height: 816px;
  }
  .card {
    position: absolute;
    width: 480px;
    height: 280px;
    background: var(--card-bg);
    border-radius: 16px;
    box-shadow: 0 2px 6px rgba(0,0,0,0.12);
  }
  .card-front { left: 140px; top: 170px; }
  .card-back  { left: 580px; top: 380px; }

  .brand {
    position: absolute;
    display: flex;
    align-items: center;
    gap: 10px;
  }
  .brand-square {
    width: 22px;
    height: 22px;
    background: var(--accent-red);
  }
  .brand-name {
    font-weight: 600;
    color: var(--ink);
    letter-spacing: 0.5px;
  }
  .card-front .brand { right: 40px; top: 64px; }
  .card-front .brand-name { font-size: 34px; }

  .holder {
    position: absolute;
    left: 0;
    top: 132px;
    padding-left: 16px;
  }
  .holder-marker {
    position: absolute;
    left: 0;
    top: 4px;
    width: 8px;
    height: 34px;
    background: var(--accent-red);
  }
  .holder-name {
    margin: 0;
    font-size: 16px;
    font-weight: 700;
    color: var(--ink);
    line-height: 1.2;
  }
  .holder-title {
    margin: 2px 0 0;
    font-size: 10.5px;
    color: var(--ink-soft);
    line-height: 1.35;
  }

  .company-address {
    position: absolute;
    left: 16px;
    top: 206px;
    margin: 0;
    font-size: 9.5px;
    line-height: 1.45;
    color: var(--ink-soft);
    font-style: normal;
  }
  .divider {
    position: absolute;
    left: 186px;
    top: 198px;
    width: 1px;
    height: 62px;
    background: var(--rule);
  }
  .contact-list {
    position: absolute;
    left: 200px;
    top: 206px;
    margin: 0;
    padding: 0;
    list-style: none;
    font-size: 9.5px;
    line-height: 1.45;
    color: var(--ink-soft);
  }

  .card-back .brand {
    left: 50%;
    top: 50%;
    transform: translate(-50%, -50%);
  }
  .card-back .brand-square { width: 30px; height: 30px; }
  .card-back .brand-name { font-size: 30px; }
</style>
</head>
<body>
<main class="canvas">
  <section class="card card-front" aria-label="Business card front">
    <div class="brand">
      <span class="brand-square"></span>
      <span class="brand-name">BrookSpan</span>
    </div>

    <div class="holder">
      <span class="holder-marker"></span>
      <h1 class="holder-name">Name Surname</h1>
      <p class="holder-title">Director, Fixed Income<br>&amp; Currencies Trading</p>
    </div>

    <address class="company-address">
      BrookSpan Associates Limited<br>
      Harbor Court 17, Oduya Close<br>
      Eastmere I Coralton I Westland
    </address>

    <span class="divider"></span>

    <ul class="contact-list">
      <li>Phone: +234 (1) 5558214</li>
      <li>Cell: +234 803 555 0147</li>
      <li>Email: Dayo@brook-span.example</li>
    </ul>
  </section>

  <section class="card card-back" aria-label="Business card back">
    <div class="brand">
      <span class="brand-square"></span>
      <span class="brand-name">BrookSpan</span>
    </div>
  </section>
</main>
</body>
</html>
```